Hadley's Groundwork Crew needs a logo/business cards.

i've just started a new Labouring Business, Called Hadley's Groundwork Crew, I provide high quality labouring servicing to local Builders and Tradesmen.
I'd like my business cards to reflect the hard work and dedication I put into my business.
I'd like to see Burnt Orange and blacks in the cards and logo.
I want my cards to catch peoples eye as there is A lot of dull business cards in my industry.

Target Market(s)

Builders and other tradesmen

Contact Information for Business Card

Hadley's Groundwork Crew

Font styles to use
Sans Serif

Colors
f78f20
ffc214
000000
ffffff

Requirements
Must have
• My name : Tom Hadley
• My Number: 0457962381
• Email Address : hadleygroundworkcrew@mailbarn.net
• A Sharp and Professional Design
Nice to have
• A unique design that separates my Cards from others,
• As I try to provide unique service to my clients I'd love my cards/logo to reflect this.

```html
<!DOCTYPE html>
<html lang="en">
<head>
<meta charset="utf-8">
<title>Hadley's Groundwork Crew – Business Card</title>
<link rel="stylesheet" href="https://fonts.googleapis.com/css2?family=Montserrat:wght@400;500;700&display=swap">
<style>
  :root {
    --burnt-orange: #f78f20;
    --amber: #ffc214;
    --ink: #1c1c1c;
    --charcoal: #2a2a2a;
    --steel: #5a5a5a;
    --paper: #ffffff;
    --backdrop: #e6e4e1;
  }
  * { box-sizing: border-box; margin: 0; padding: 0; }
  html, body { width: 1200px; height: 900px; overflow: hidden; }
  body {
    background: var(--backdrop);
    font-family: "Montserrat", Arial, sans-serif;
    color: var(--ink);
    position: relative;
  }
  .card {
    position: absolute;
    left: 250px;
    width: 700px;
    height: 400px;
    overflow: hidden;
    box-shadow: 0 6px 18px rgba(0,0,0,.18);
  }
  .card--front { top: 40px; background: var(--paper); }
  .card--back {
    top: 470px;
    background: linear-gradient(160deg, #3a3a3a 0%, var(--charcoal) 45%, #111 100%);
    display: flex;
    align-items: center;
    justify-content: center;
  }
  .wordmark {
    font-weight: 700;
    color: var(--burnt-orange);
    text-transform: uppercase;
    letter-spacing: 1px;
    line-height: 1.05;
  }
  .card--front .wordmark {
    position: absolute;
    left: 44px;
    top: 58px;
    font-size: 34px;
  }
  .wordmark__sub { display: block; font-size: .58em; letter-spacing: 2px; }
  .card--back .wordmark { font-size: 58px; text-align: left; }
  .person {
    position: absolute;
    right: 44px;
    top: 64px;
    text-align: right;
  }
  .person__name {
    font-size: 26px;
    font-weight: 500;
    color: var(--burnt-orange);
    letter-spacing: 2px;
    text-transform: uppercase;
  }
  .person__role { font-size: 15px; margin-top: 2px; letter-spacing: 1px; }
  .divider {
    position: absolute;
    left: 44px;
    right: 44px;
    top: 172px;
    height: 2px;
    background: var(--burnt-orange);
  }
  .contacts {
    position: absolute;
    left: 44px;
    top: 192px;
    list-style: none;
    font-size: 15px;
    line-height: 24px;
    letter-spacing: .5px;
  }
  .contacts li { display: flex; align-items: center; gap: 10px; }
  .contacts svg { width: 14px; height: 14px; flex: none; }
  .address {
    position: absolute;
    right: 44px;
    top: 192px;
    text-align: right;
    font-style: normal;
    font-size: 15px;
    line-height: 24px;
    letter-spacing: .5px;
  }
  .wave { position: absolute; left: 0; bottom: 0; width: 700px; height: 400px; }
</style>
</head>
<body>

<section class="card card--front" aria-label="Business card front">
  <div class="wordmark">Hadley's<span class="wordmark__sub">Groundwork Crew</span></div>

  <div class="person">
    <div class="person__name">Tom Hadley</div>
    <div class="person__role">Director</div>
  </div>

  <div class="divider"></div>

  <ul class="contacts">
    <li>
      <svg viewBox="0 0 16 16"><path d="M4 1.5l2.3 3-1.4 1.6c.9 2 2.4 3.6 4.4 4.6l1.6-1.4 3 2.3-1.4 2.4C7 13.8 2.2 9 1.6 2.9z" fill="var(--burnt-orange)"/></svg>
      0457 962 381
    </li>
    <li>
      <svg viewBox="0 0 16 16"><rect x="1.5" y="3.5" width="13" height="9" fill="none" stroke="var(--burnt-orange)" stroke-width="1.6"/><path d="M1.5 3.5l6.5 5 6.5-5" fill="none" stroke="var(--burnt-orange)" stroke-width="1.6"/></svg>
      hadleygroundworkcrew@mailbarn.net
    </li>
    <li>
      <svg viewBox="0 0 16 16"><circle cx="8" cy="8" r="6.2" fill="none" stroke="var(--burnt-orange)" stroke-width="1.5"/><path d="M1.8 8h12.4M8 1.8c-3 3.4-3 9 0 12.4M8 1.8c3 3.4 3 9 0 12.4" fill="none" stroke="var(--burnt-orange)" stroke-width="1.2"/></svg>
      www.hadleygroundwork.net
    </li>
  </ul>

  <address class="address">
    1920 Quarry Lane<br>
    Millbrook, TX 78410
  </address>

  <svg class="wave" viewBox="0 0 700 400" aria-hidden="true">
    <defs>
      <linearGradient id="waveOrange" x1="0" y1="0" x2="1" y2="0">
        <stop offset="0" stop-color="var(--amber)"/>
        <stop offset="1" stop-color="var(--burnt-orange)"/>
      </linearGradient>
    </defs>
    <path d="M0 400 L0 392 C200 394 380 335 520 306 C600 290 660 290 700 296 L700 400 Z" fill="url(#waveOrange)"/>
    <path d="M0 384 C200 388 380 326 520 296 C600 281 660 281 700 287" fill="none" stroke="var(--steel)" stroke-width="4"/>
  </svg>
</section>

<section class="card card--back" aria-label="Business card back">
  <div class="wordmark">Hadley's<span class="wordmark__sub">Groundwork Crew</span></div>
</section>

</body>
</html>
```